Wordpress website design needed for website re-launch of established lawn care company (Design mu...

We are a gardening company and are separating and re-launching the lawn care part of the company. We already have a non-wordpress website which includes a lawn care section and therefore contains all the content needed for the new website. We essentially need to take that content (over 6 pages) and re-create it into a new, modern and visually appealing design in our new Wordpress website. We use Divi and therefore the new design must be built and be compatible with the Divi theme. However, I am not looking to use a pre-built Divi layout or any template offered by Quarry Layouts. I could easily do that myself. I'm looking for a bespoke design.

The pages of our current website that need to be re-designed within Divi are:
http://www.brackettgrounds.co.uk/lawncare/7281604452
http://www.brackettgrounds.co.uk/lawnfertilisers/7281619038
http://www.brackettgrounds.co.uk/lawnaeration/7281652271
http://www.brackettgrounds.co.uk/lawnscarification/7281658815
http://www.brackettgrounds.co.uk/lawntreatments/7281663340
http://www.brackettgrounds.co.uk/lawncarepackages/7281619177

Our Wordpress site is already set up with Veltra with the domain www.brackettturfcare.co.uk and as I say, uses the Divi theme. I am not sure how you will deliver your designs but it must be using or compatible with Divi.

Target Market(s)

Homeowners ages 30+

Industry/Entity Type

Gardener

Font styles to use
Sans Serif

Colors
a64599
9bcb3c

Requirements
Must have
• The new site must still use our existing company colours - purple and green. Have a look on www.brackettgrounds.co.uk to get the right colours.
• Must be mobile responsive
Nice to have
• We want a fresh and modern new look for our new lawn care website.
• I have also attached a picture of our van and lawn care flyers so you can see what our current branding and style looks like in case it helps with your design.
Should not have
• Please don't just submit pre-designed templates that bear no relevance to my brief or requirements above. I could very easily go and install a pre-designed template and plug my content in but that's not what I'm looking for. Submissions should take into consideration my existing content, my brand colours and my logo as a minimum.

```html
<!DOCTYPE html>
<html lang="en">
<head>
<meta charset="utf-8">
<title>Brackett Turf Care Services</title>
<link href="https://fonts.googleapis.com/css2?family=Raleway:wght@400;500;600;700&display=swap" rel="stylesheet">
<style>
:root{
  --green:#8dc63f;
  --green-dark:#6fa52a;
  --purple:#a64599;
  --ink:#1d1d1d;
  --text:#444;
  --muted:#777;
  --line:#e2e2e2;
  --panel:#f2f2f2;
  --footer:#141414;
  --white:#fff;
}
*{box-sizing:border-box;margin:0;padding:0}
html,body{width:1200px;height:3930px;overflow:hidden;background:var(--white)}
body{font-family:"Raleway",sans-serif;color:var(--text)}
.page{position:relative;width:1200px;height:3930px;overflow:hidden}
.abs{position:absolute}
.btn{position:absolute;display:flex;align-items:center;justify-content:center;border-radius:20px;font-size:13px;font-weight:600}
.btn-green{background:var(--green);color:var(--white)}

/* header */
.topbar{left:524px;top:0;width:676px;height:47px;background:var(--green);border-bottom-left-radius:40px}
.contact{top:15px;font-size:12px;color:var(--white);display:flex;align-items:center;gap:7px;white-space:nowrap}
.social{top:10px;width:26px;height:26px;border-radius:50%;background:var(--white)}
.brand{left:157px;top:22px;display:flex;align-items:center;gap:10px;font-size:26px;font-weight:700;color:var(--purple)}
.brand-mark{width:34px;height:34px;border-radius:50%;background:var(--green)}
.nav{top:74px;font-size:13px;color:var(--ink);font-weight:500}
.nav-home{left:560px;top:66px;width:76px;height:32px;border-radius:18px;background:var(--green);color:var(--white);display:flex;align-items:center;justify-content:center;font-size:13px}

/* hero */
.hero-photo{left:0;top:118px;width:1200px;height:607px;background:linear-gradient(160deg,#b7c98b 0%,#6d8f3e 45%,#3f6a22 100%)}
.hero-title{left:92px;top:285px;font-size:38px;font-weight:700;line-height:48px;color:var(--ink);letter-spacing:.5px}
.hero-btn{left:92px;top:448px;width:124px;height:38px;background:#2c2c2c;color:var(--white);border-radius:8px;font-size:13px}

/* welcome */
.eyebrow{left:157px;top:778px;font-size:12px;color:var(--ink)}
.welcome-title{left:157px;top:810px;font-size:24px;font-weight:600;color:var(--ink)}
.welcome-text{left:157px;top:868px;width:432px;font-size:12.5px;line-height:24px;color:var(--text)}
.thumb{top:843px;height:250px}

/* projects */
.projects-panel{left:0;top:1181px;width:298px;height:375px;background:var(--green)}
.projects-title{left:36px;top:1252px;font-size:24px;color:var(--white);font-weight:500}
.projects-title b{font-weight:700}
.projects-text{left:36px;top:1320px;width:230px;font-size:12px;line-height:24px;color:var(--white)}
.projects-btn{left:36px;top:1447px;width:128px;height:40px;background:var(--white);color:#bbb;font-weight:500}
.slide{top:1181px;height:375px}
.arrow{top:1348px;width:30px;height:44px;background:var(--white);display:flex;align-items:center;justify-content:center}

/* section titles */
.section-title{left:0;width:1200px;text-align:center;font-size:34px;color:var(--ink);font-weight:500}
.section-title span{color:var(--green);font-weight:700}
.rule{left:556px;width:88px;height:3px;background:var(--green)}

/* services */
.tabs{left:141px;top:1718px;width:367px;border:1px solid var(--line)}
.tab{height:60px;border-bottom:1px solid var(--line);display:flex;align-items:center;padding-left:22px;gap:18px;font-size:14px;color:var(--ink)}
.tab:last-child{border-bottom:none}
.tab.active{background:var(--green);color:var(--white)}
.tab svg{width:20px;height:20px}
.service-panel{left:534px;top:1718px;width:524px;height:525px;background:var(--panel)}
.service-img{left:558px;top:1750px;width:477px;height:194px;background:linear-gradient(180deg,#b94a3a 0%,#6e8e46 40%,#4f7a2c 100%)}
.service-title{left:563px;top:1982px;font-size:19px;font-weight:700;color:var(--ink)}
.service-text{left:563px;top:2030px;width:460px;font-size:12.5px;line-height:27px;color:var(--text)}
.service-btn{left:563px;top:2162px;width:118px;height:40px}

/* testimonials */
.testimonial-bg{left:0;top:2318px;width:1200px;height:556px;background:radial-gradient(ellipse at 50% 40%,#3f6a26 0%,#22401a 55%,#132610 100%)}
.testimonial-title{top:2384px;color:var(--white)}
.quote-card{top:2489px;width:289px;height:165px;background:var(--green);color:var(--white);font-size:12px;line-height:22px;padding:22px 20px;text-align:center}
.quote-mark{top:2626px;width:56px;height:56px;border-radius:50%;background:var(--white);display:flex;align-items:center;justify-content:center}
.avatar{top:2711px;width:80px;height:80px;border-radius:50%;background:linear-gradient(180deg,#d9d2c8,#8c7f72);border:3px solid var(--white)}
.client-name{top:2734px;font-size:14px;font-weight:700;color:var(--white)}
.client-role{top:2760px;font-size:12px;color:var(--white)}

/* blog */
.blog-card{top:3039px;width:289px;height:419px;background:var(--panel)}
.blog-img{top:3039px;width:289px;height:236px}
.blog-date{top:3300px;font-size:12px;color:var(--ink)}
.blog-title{top:3340px;width:250px;font-size:20px;font-weight:700;line-height:30px;color:var(--ink)}
.blog-more{top:3413px;font-size:14px;color:var(--green)}

/* footer */
.footer{left:0;top:3518px;width:1200px;height:380px;background:var(--footer)}
.footer-brand{left:157px;top:3612px;display:flex;align-items:center;gap:10px;font-size:24px;font-weight:700;color:var(--white)}
.footer-mark{width:30px;height:30px;border-radius:50%;background:var(--purple)}
.footer-about{left:144px;top:3697px;width:205px;font-size:11.5px;line-height:20px;color:#ccc}
.footer-social{top:3815px;width:20px;height:20px;border-radius:4px;background:var(--white)}
.footer-head{top:3577px;font-size:18px;font-weight:700;color:var(--white)}
.footer-label{font-size:12px;font-weight:700;color:var(--white)}
.footer-val{font-size:11px;line-height:19px;color:#ccc}
.footer-link{left:661px;font-size:12px;color:#ddd}
.newsletter-input{left:856px;top:3706px;width:204px;height:38px;border-radius:20px;background:var(--white);font-size:10px;color:#999;padding:13px 16px}
.newsletter-btn{left:856px;top:3750px;width:204px;height:36px;font-size:11px;font-weight:700}
.copyright{left:0;top:3898px;width:1200px;height:32px;background:var(--green);color:var(--ink);font-size:12px;display:flex;align-items:center;justify-content:center}
</style>
</head>
<body>
<div class="page">

  <!-- header -->
  <div class="abs topbar"></div>
  <div class="abs contact" style="left:556px">
    <svg width="13" height="13" viewBox="0 0 24 24" fill="#fff"><path d="M6.6 10.8a15 15 0 0 0 6.6 6.6l2.2-2.2c.3-.3.7-.4 1-.2 1.1.4 2.3.6 3.6.6.6 0 1 .4 1 1V20c0 .6-.4 1-1 1A17 17 0 0 1 3 4c0-.6.4-1 1-1h3.5c.6 0 1 .4 1 1 0 1.3.2 2.5.6 3.6.1.3 0 .7-.2 1z"/></svg>
    01632 960418
  </div>
  <div class="abs contact" style="left:676px">
    <svg width="13" height="10" viewBox="0 0 24 18" fill="#fff"><path d="M0 0h24v18H0zM2 2l10 7 10-7v-0.5H2z" fill-rule="evenodd"/></svg>
    enquiries@brackettgrounds.co.uk
  </div>
  <div class="abs social" style="left:914px"></div>
  <div class="abs social" style="left:948px"></div>

  <div class="abs brand"><span class="brand-mark"></span>Brackett Turf Care</div>

  <div class="abs nav-home">Home</div>
  <div class="abs nav" style="left:664px">About Lawn Care</div>
  <div class="abs nav" style="left:807px">Services</div>
  <div class="abs nav" style="left:899px">Gallery</div>
  <div class="abs nav" style="left:986px">Contact Us</div>

  <!-- hero -->
  <div class="abs hero-photo" role="img" aria-label="Close view of a lawn mower cutting a green lawn beside a garden play house"></div>
  <svg class="abs" style="left:0;top:118px" width="1200" height="607" viewBox="0 0 1200 607">
    <defs>
      <linearGradient id="heroFade" x1="0" y1="0" x2="1" y2="0">
        <stop offset="0" stop-color="#9ccf4a"/>
        <stop offset="1" stop-color="#7db834"/>
      </linearGradient>
    </defs>
    <polygon points="0,0 500,0 250,607 0,607" fill="url(#heroFade)"/>
    <polygon points="500,0 580,0 300,607 250,607" fill="#a7d65a" opacity=".55"/>
    <polygon points="1100,280 1200,200 1200,420 980,607 900,607" fill="#8dc63f" opacity=".9"/>
    <polygon points="0,560 200,607 0,607" fill="#fff"/>
    <polygon points="900,607 1200,520 1200,607" fill="#fff"/>
  </svg>
  <div class="abs hero-title">EXPERT LAWN<br>TREATMENT<br>SERVICE</div>
  <div class="btn hero-btn">LEARN MORE</div>

  <!-- welcome -->
  <div class="abs eyebrow">Welcome To Our</div>
  <div class="abs welcome-title">Brackett Turf Care Services</div>
  <p class="abs welcome-text">As expert gardeners, we are passionate about horticulture and working to bring out the very best in your garden. When we work in your garden, we look at it and treat it with the same care and attention as if it were our own, before handing it back for you to enjoy. Our passion doesn't end with just trees and shrubs, though. Your grass is as much of a living, breathing plant as your shrubs and we therefore utilise our expert horticultural knowledge to ensure your lawn thrives and reaches its fullest potential.</p>
  <div class="btn btn-green" style="left:157px;top:1079px;width:126px;height:40px">Read More</div>
  <div class="abs thumb" style="left:610px;width:218px;background:linear-gradient(180deg,#8fb070 0%,#a78b6a 55%,#6f9a3d 100%)" role="img" aria-label="Garden path lined with neat flower beds and lawn"></div>
  <div class="abs thumb" style="left:838px;width:220px;background:linear-gradient(180deg,#5d6b3a 0%,#d6b43a 45%,#6fae35 100%)" role="img" aria-label="Yellow lawn scarifying machine on grass"></div>

  <!-- projects -->
  <div class="abs projects-panel"></div>
  <div class="abs projects-title">Our <b>Projects</b></div>
  <p class="abs projects-text">Lorem Ipsum is simply dummy text of the printing and typesetting industry. Lorem Ipsum has been the industry's standard dummy text ever.</p>
  <div class="btn projects-btn">Read More</div>
  <div class="abs slide" style="left:298px;width:300px;background:linear-gradient(180deg,#cfe0ee 0%,#9a8775 45%,#5f8a34 100%)" role="img" aria-label="Cottage house with lawn and garden"></div>
  <div class="abs slide" style="left:598px;width:300px;background:linear-gradient(180deg,#4e7a2e 0%,#7db84a 50%,#5d9630 100%)" role="img" aria-label="Gardener pushing a mower across a striped lawn"></div>
  <div class="abs slide" style="left:898px;width:302px;background:linear-gradient(180deg,#cfdde8 0%,#a4553f 40%,#5e8f34 100%)" role="img" aria-label="Red roofed house with front lawn"></div>
  <div class="abs arrow" style="left:298px"><svg width="12" height="16" viewBox="0 0 12 16"><path d="M10 1 3 8l7 7" stroke="#333" stroke-width="3" fill="none"/></svg></div>
  <div class="abs arrow" style="left:1170px"><svg width="12" height="16" viewBox="0 0 12 16"><path d="M2 1l7 7-7 7" stroke="#333" stroke-width="3" fill="none"/></svg></div>

  <!-- services -->
  <div class="abs section-title" style="top:1612px">Our <span>Services</span></div>
  <div class="abs rule" style="top:1662px"></div>
  <div class="abs tabs">
    <div class="tab active"><svg viewBox="0 0 20 20"><path d="M3 17c2-4 4-6 7-7M10 17V8M17 17c-2-4-4-6-7-7" stroke="currentColor" stroke-width="2" fill="none"/></svg>Spring Treatment</div>
    <div class="tab"><svg viewBox="0 0 20 20"><path d="M2 16h16M4 16v-4M8 16v-6M12 16v-5M16 16v-4" stroke="var(--green)" stroke-width="2" fill="none"/></svg>Early Summer Treatment</div>
    <div class="tab"><svg viewBox="0 0 20 20"><path d="M3 17c2-4 4-6 7-7M10 17V8M17 17c-2-4-4-6-7-7" stroke="var(--green)" stroke-width="2" fill="none"/></svg>Late Summer Treatment</div>
    <div class="tab"><svg viewBox="0 0 20 20"><path d="M4 17 10 4l6 13" stroke="var(--green)" stroke-width="2" fill="none"/></svg>Autumn Treatment</div>
    <div class="tab"><svg viewBox="0 0 20 20"><path d="M4 17c1-5 3-8 6-10M10 17V6M16 17c-1-5-3-8-6-10" stroke="var(--green)" stroke-width="2" fill="none"/></svg>Aeration</div>
    <div class="tab"><svg viewBox="0 0 20 20"><rect x="3" y="8" width="14" height="6" fill="var(--green)"/><circle cx="6" cy="16" r="2" fill="var(--green)"/><circle cx="14" cy="16" r="2" fill="var(--green)"/></svg>Scarification</div>
    <div class="tab"><svg viewBox="0 0 20 20"><rect x="4" y="6" width="12" height="10" fill="var(--green)"/></svg>GrowSlow</div>
    <div class="tab"><svg viewBox="0 0 20 20"><path d="M4 5h12M4 10h12M4 15h12" stroke="var(--green)" stroke-width="2.5"/></svg>Hydration Boost</div>
    <div class="tab"><svg viewBox="0 0 20 20"><rect x="3" y="3" width="6" height="6" fill="var(--green)"/><rect x="11" y="3" width="6" height="6" fill="var(--green)"/><rect x="3" y="11" width="6" height="6" fill="var(--green)"/><rect x="11" y="11" width="6" height="6" fill="var(--green)"/></svg>Turfing &amp; Renovation</div>
  </div>
  <div class="abs service-panel"></div>
  <div class="abs service-img" role="img" aria-label="Lawn spreader applying granular feed to grass"></div>
  <div class="abs service-title">Spring Treatment</div>
  <p class="abs service-text">Lorem Ipsum is simply dummy text of the printing and typesetting industry. Lorem Ipsum has been the industry's standard dummy text ever since the 1500s, when an unknown printer took a galley of type and scrambled it to make a type specimen book. It has survived not only five centuries.</p>
  <div class="btn btn-green service-btn">Read More</div>

  <!-- testimonials -->
  <div class="abs testimonial-bg" role="img" aria-label="Dark close-up of long grass blades"></div>
  <div class="abs section-title testimonial-title" style="color:var(--white)">Our <span>Testimonial</span></div>
  <div class="abs rule" style="top:2434px"></div>

  <p class="abs quote-card" style="left:141px">Lorem Ipsum is simply dummy text of the printing and typesetting industry. Lorem Ipsum has been the industry's standard dummy text ever since the 1500s.</p>
  <p class="abs quote-card" style="left:456px">Lorem Ipsum is simply dummy text of the printing and typesetting industry. Lorem Ipsum has been the industry's standard dummy text ever since the 1500s.</p>
  <p class="abs quote-card" style="left:770px">Lorem Ipsum is simply dummy text of the printing and typesetting industry. Lorem Ipsum has been the industry's standard dummy text ever since the 1500s.</p>

  <div class="abs quote-mark" style="left:162px"><svg width="24" height="18" viewBox="0 0 24 18"><path d="M2 2h6v8l-3 6H2l2-6H2zM14 2h6v8l-3 6h-3l2-6h-2z" fill="#222"/></svg></div>
  <div class="abs quote-mark" style="left:477px"><svg width="24" height="18" viewBox="0 0 24 18"><path d="M2 2h6v8l-3 6H2l2-6H2zM14 2h6v8l-3 6h-3l2-6h-2z" fill="#222"/></svg></div>
  <div class="abs quote-mark" style="left:791px"><svg width="24" height="18" viewBox="0 0 24 18"><path d="M2 2h6v8l-3 6H2l2-6H2zM14 2h6v8l-3 6h-3l2-6h-2z" fill="#222"/></svg></div>

  <div class="abs avatar" style="left:152px" role="img" aria-label="Client portrait"></div>
  <div class="abs client-name" style="left:246px">Name Here</div>
  <div class="abs client-role" style="left:246px">Client</div>
  <div class="abs avatar" style="left:466px" role="img" aria-label="Client portrait"></div>
  <div class="abs client-name" style="left:560px">Name Here</div>
  <div class="abs client-role" style="left:560px">Client</div>
  <div class="abs avatar" style="left:780px" role="img" aria-label="Client portrait"></div>
  <div class="abs client-name" style="left:874px">Name Here</div>
  <div class="abs client-role" style="left:874px">Client</div>

  <!-- blog -->
  <div class="abs section-title" style="top:2930px">Our <span>Blog</span></div>
  <div class="abs rule" style="top:2980px"></div>

  <div class="abs blog-card" style="left:141px"></div>
  <div class="abs blog-img" style="left:141px;background:linear-gradient(180deg,#8fa86a 0%,#c9c3b5 55%,#6e9a42 100%)" role="img" aria-label="Patio garden with parasol and seating"></div>
  <div class="abs blog-date" style="left:163px">April 19,2019</div>
  <div class="abs blog-title" style="left:163px">Lorem Ipsum is simply dummy text of the</div>
  <div class="abs blog-more" style="left:163px">More»</div>

  <div class="abs blog-card" style="left:456px"></div>
  <div class="abs blog-img" style="left:456px;background:linear-gradient(180deg,#a9c8e6 0%,#e8e8e6 45%,#6ea23a 100%)" role="img" aria-label="Large white house with palm trees and wide lawn"></div>
  <div class="abs blog-date" style="left:478px">April 19,2019</div>
  <div class="abs blog-title" style="left:478px">Lorem Ipsum is simply dummy text of the</div>
  <div class="abs blog-more" style="left:478px">More»</div>

  <div class="abs blog-card" style="left:770px"></div>
  <div class="abs blog-img" style="left:770px;background:linear-gradient(180deg,#c7cba6 0%,#9cc25b 50%,#5f8f2c 100%)" role="img" aria-label="Close-up of fresh green grass"></div>
  <div class="abs blog-date" style="left:792px">April 19,2019</div>
  <div class="abs blog-title" style="left:792px">Lorem Ipsum is simply dummy text of the</div>
  <div class="abs blog-more" style="left:792px">More»</div>

  <!-- footer -->
  <div class="abs footer"></div>
  <div class="abs footer-brand"><span class="footer-mark"></span>Brackett</div>
  <p class="abs footer-about">"Sed ut perspiciatis unde omnis iste natus error sit voluptatem accusantium doloremque laudantium, totam rem aperiam.</p>
  <div class="abs footer-social" style="left:147px"></div>
  <div class="abs footer-social" style="left:187px"></div>

  <div class="abs footer-head" style="left:416px">Head Office</div>
  <div class="abs footer-label" style="left:416px;top:3624px">Address</div>
  <div class="abs footer-val" style="left:416px;top:3643px;width:230px;white-space:nowrap">Meadow Business Park Fenwick Close<br>Ashbury AB1 2CD</div>
  <div class="abs footer-label" style="left:416px;top:3695px">E-mail</div>
  <div class="abs footer-val" style="left:416px;top:3714px">enquiries@brackettgrounds.co.uk</div>
  <div class="abs footer-label" style="left:416px;top:3750px">Phone</div>
  <div class="abs footer-val" style="left:416px;top:3769px">01632 960418</div>

  <div class="abs footer-head" style="left:661px">Quick Links</div>
  <div class="abs footer-link" style="top:3630px">Home</div>
  <div class="abs footer-link" style="top:3668px">About Us</div>
  <div class="abs footer-link" style="top:3706px">Services</div>
  <div class="abs footer-link" style="top:3744px">Gallery</div>
  <div class="abs footer-link" style="top:3782px">Blog</div>
  <div class="abs footer-link" style="top:3820px">Contact Us</div>

  <div class="abs footer-head" style="left:856px">Newstletter</div>
  <p class="abs footer-val" style="left:856px;top:3620px;width:204px">Stay always in touch! Subscribe to our newsletter</p>
  <div class="abs newsletter-input">Your Email</div>
  <div class="btn btn-green newsletter-btn">SUBSCRIBE</div>
  <div class="abs footer-val" style="left:856px;top:3796px;font-size:10px">* Don't worry, we don't spam</div>

  <div class="abs copyright">Copyright © 2019 Brackett Turf Care Services. All Rights Reserved</div>
</div>
</body>
</html>
```